Leading Nutrition Company Needs a Stylish Label Design!

We need a label/packaging design for our new cutting-edge detox called "Clear Tide". It is an all organic detox that removes toxins, harsh-chemicals, herbicides, pesticides and heavy metals from the body. It essentially turns everything you eat into organic whole foods and without all the chemicals in our bodies, we run at optimal performance.

We are attempting to blend a modern, simplistic design for our label.
We would like to see designs that use flat grays, silvers and blacks. We would also like to see pops of green and or blue in the design. Overall design will be a modern, contemporary matte finish with pops of color in either a pattern design or colored lettering. The final design should convey a high-end, exclusive health product.

Target Market(s)

Health conscious individuals and those seeking to pass an upcoming drug test. Athletes, nutritionist, dietitians ranging from 18-70 years of age.

Industry/Entity Type

Health

Font styles to use
Other font styles liked:
• Unique modern fonts

Colors
b1b1b1
9d9d9d
474747
33a6d7
0192cd
9ccb3b

Requirements
Must have
• Must be modern and simplistic

Pops of color - Don't need to be matte

Matte finishes for background
-Light grays, graphite, light silvers etc

Lettering must be modern and unique

Label type wil be a "shrink label" for an 8 oz boston squat bottle
-See attached link for bottle

"Clear Tide" some where on label

Company logo some where on label
-See attached files for logo
Nice to have
• Cool background designs that provide depth to the design.

A strip of pattern design running vertically or horizontally to capture the eye.
-See attached pictures for examples
Should not have
• Script or Normal fonts

```html
<!DOCTYPE html>
<html lang="en">
<head>
<meta charset="utf-8">
<title>Clear Tide – Detox Label</title>
<link rel="stylesheet" href="https://fonts.googleapis.com/css2?family=Saira+Condensed:wght@500&family=Exo+2:wght@400;500&display=swap">
<style>
  :root {
    --graphite: #474747;
    --graphite-light: #555555;
    --graphite-dark: #3c3c3c;
    --lime: #a6d11f;
    --lime-deep: #9ccb3b;
    --silver: #c9c9c9;
    --white: #ffffff;
    --ink: #3d3d3d;
  }
  * { margin: 0; padding: 0; box-sizing: border-box; }
  html, body { width: 994px; height: 1200px; overflow: hidden; }
  body { background: var(--graphite); font-family: "Exo 2", sans-serif; }

  .label {
    position: relative;
    width: 994px;
    height: 1200px;
    overflow: hidden;
  }
  .label__texture {
    position: absolute;
    inset: 0;
    background: linear-gradient(135deg, var(--graphite-light) 0%, var(--graphite) 45%, var(--graphite-dark) 100%);
  }
  .label__arc {
    position: absolute;
    inset: 0;
  }

  .name-block {
    position: absolute;
    left: 267px;
    top: 250px;
    width: 460px;
    height: 440px;
    background: var(--lime);
    text-align: center;
    overflow: hidden;
  }
  .name-block__tab {
    position: absolute;
    left: 50%;
    top: 0;
    transform: translateX(-50%);
    width: 200px;
    height: 52px;
    background: var(--graphite);
    color: var(--white);
    font-family: "Exo 2", sans-serif;
    font-weight: 500;
    font-size: 40px;
    line-height: 44px;
  }
  .name-block__title {
    font-weight: 500;
  }
  .name-block__line {
    display: block;
    font-family: "Saira Condensed", sans-serif;
    font-weight: 500;
    font-size: 160px;
    line-height: 1;
    letter-spacing: 1px;
    white-space: nowrap;
  }
  .name-block__line--top {
    margin-top: 66px;
    color: var(--ink);
  }
  .name-block__line--bottom {
    margin-top: 8px;
    color: var(--white);
  }

  .flavour {
    position: absolute;
    left: 0;
    top: 730px;
    width: 994px;
    text-align: center;
    color: var(--silver);
    font-family: "Exo 2", sans-serif;
    font-size: 44px;
    line-height: 54px;
  }

  .maker {
    position: absolute;
    left: 600px;
    top: 950px;
    display: flex;
    align-items: center;
    gap: 14px;
  }
  .maker__dot {
    width: 28px;
    height: 28px;
    border-radius: 50%;
    background: var(--white);
  }
  .maker__name {
    color: var(--white);
    font-family: "Exo 2", sans-serif;
    font-weight: 500;
    font-size: 34px;
  }

  .volume {
    position: absolute;
    left: 0;
    top: 1115px;
    width: 994px;
    text-align: center;
    color: var(--white);
    font-family: "Exo 2", sans-serif;
    font-weight: 500;
    font-size: 42px;
  }
</style>
</head>
<body>
  <main class="label">
    <div class="label__texture" role="img" aria-label="Faint faceted low-poly pattern in graphite tones across the label background"></div>

    <svg class="label__arc" width="994" height="1200" viewBox="0 0 994 1200" aria-hidden="true">
      <path d="M 264 870 A 500 500 0 0 0 140 1200" fill="none" stroke="var(--lime-deep)" stroke-width="48"/>
    </svg>

    <section class="name-block">
      <span class="name-block__tab">detox</span>
      <h1 class="name-block__title">
        <span class="name-block__line name-block__line--top">CLEAR</span>
        <span class="name-block__line name-block__line--bottom">TIDE</span>
      </h1>
    </section>

    <p class="flavour">aloe vera, apple<br>&amp; blueberry juice</p>

    <div class="maker">
      <span class="maker__dot"></span>
      <span class="maker__name">Verdant Labs</span>
    </div>

    <p class="volume">18.8 FL OZ (319ml)</p>
  </main>
</body>
</html>
```